Design template for news articles we will share with clients and prospects -

We have some client ready articles written that we would like to have a template created that we can use going forward to publish them on. I uploaded 4 examples including our company color palette. I also have 3 examples of articles we would want to incorporate into the template once we have it. They are marked (unbranded)

We want a template where we can add those unbranded materials and then publish and share them with clients.
Updates

Target Market(s)

Clients and prospects

Industry/Entity Type

Financial Service

Requirements
Must have
• The template should be able to easily add client ready written articles.
Should not have
• We aren't looking for just a simple letterhead.

```html
<!DOCTYPE html>
<html lang="en">
<head>
<meta charset="utf-8">
<title>Estate Planning – Article Template</title>
<link href="https://fonts.googleapis.com/css2?family=Tinos:wght@400;700&family=Didact+Gothic&display=swap" rel="stylesheet">
<style>
  :root{
    --backdrop:#e9e9ea;
    --paper:#ffffff;
    --ink:#3f3f42;
    --ink-soft:#5a5a5e;
    --heading:#2f2f33;
    --accent-blue:#8aa3c4;
    --accent-green:#3d4f22;
    --accent-gold:#b39a5c;
    --stripe-lavender:#c9c8e0;
    --stripe-grey:#d3d3d6;
    --stripe-sage:#c9cfb8;
  }
  *{box-sizing:border-box;margin:0;padding:0}
  html,body{width:1200px;height:795px;overflow:hidden;background:var(--backdrop)}
  .sheet{
    position:absolute;left:315px;top:22px;width:570px;height:750px;
    background:var(--paper);box-shadow:0 2px 10px rgba(0,0,0,.12);
    font-family:"Didact Gothic",sans-serif;color:var(--ink);
  }
  .header-rule{position:absolute;left:44px;top:98px;width:290px;height:2px;background:var(--accent-blue)}
  .brand{position:absolute;right:44px;top:58px;display:flex;align-items:center;gap:8px}
  .brand-mark{width:14px;height:14px;background:var(--accent-green)}
  .brand-name{font-family:"Didact Gothic",sans-serif;font-size:24px;letter-spacing:1px;color:var(--heading)}
  .article{position:absolute;left:44px;top:126px;width:470px}
  .article-title{font-family:"Tinos",serif;font-weight:700;font-size:21px;color:var(--heading);line-height:1.1}
  .intro{font-size:10px;line-height:1.35;color:var(--ink-soft);margin-bottom:10px}
  .section{margin-bottom:12px}
  .section-title{font-family:"Tinos",serif;font-weight:700;font-size:12.5px;color:var(--heading);line-height:1.2;margin-left:12px}
  .section-text{font-size:10px;line-height:1.35;color:var(--ink-soft);margin-left:12px}
  .decisions{margin:6px 0 0 24px}
  .decisions-label{font-family:"Tinos",serif;font-weight:700;font-size:12px;color:var(--accent-gold)}
  .decisions ul{list-style:none;font-size:10px;line-height:1.3;color:var(--ink-soft)}
  .decisions li::before{content:"•";margin-right:4px;color:var(--ink)}
  .footer-rule{position:absolute;left:215px;right:44px;top:664px;height:2px;background:var(--accent-green)}
  .footer-stripes{position:absolute;left:38px;bottom:0;width:90px;height:110px}
  .footer-contact{position:absolute;left:130px;top:688px;font-size:11px;color:var(--ink)}
</style>
</head>
<body>
  <div class="sheet">
    <div class="header-rule"></div>
    <div class="brand">
      <span class="brand-mark"></span>
      <span class="brand-name">MERIDIAN</span>
    </div>

    <article class="article">
      <h1 class="article-title">Estate Planning</h1>
      <p class="intro">Multiple legal documents that protect you and your spouse in unfortunate circumstances such as death or disability</p>

      <section class="section">
        <h2 class="section-title">Wills</h2>
        <p class="section-text">Documents that specify your wishes, including how you want your property distributed, who will administer your estate, and who will care for your minor children</p>
        <div class="decisions">
          <h3 class="decisions-label">Decisions</h3>
          <ul><li>Executor</li><li>Successor</li><li>Property disposition</li><li>Guardian for minor children</li></ul>
        </div>
      </section>

      <section class="section">
        <h2 class="section-title">Health Care Power of Attorney</h2>
        <p class="section-text">Document that appoints someone to make decisions about your medical treatment if you are unable to make them yourself</p>
        <div class="decisions">
          <h3 class="decisions-label">Decisions</h3>
          <ul><li>Name the power holder</li><li>Successor</li></ul>
        </div>
      </section>

      <section class="section">
        <h2 class="section-title">Living Will (Advanced Medial Directives)</h2>
        <p class="section-text">Document which describes your preferences for end-of-life care if you are unable to make decisions for yourself</p>
        <div class="decisions">
          <h3 class="decisions-label">Decisions</h3>
          <ul><li>Multiple questions about potential treatment</li></ul>
        </div>
      </section>

      <section class="section">
        <h2 class="section-title">Durable Power of Attorney</h2>
        <p class="section-text">Document that appoints someone to act for you in financial matters, so that someone can pay your bills, make financial decision, etc. if you are unable to. The document is usually prepared so as to be effective only upon your incapacity, but can be prepared to be effective immediately.</p>
        <div class="decisions">
          <h3 class="decisions-label">Decisions</h3>
          <ul><li>Name the power holder</li><li>Successor</li></ul>
        </div>
      </section>
    </article>

    <div class="footer-rule"></div>
    <svg class="footer-stripes" viewBox="0 0 90 110" aria-hidden="true">
      <rect x="4" y="10" width="4" height="100" fill="var(--stripe-lavender)"/>
      <rect x="14" y="30" width="4" height="80" fill="var(--stripe-grey)"/>
      <rect x="24" y="50" width="4" height="60" fill="var(--stripe-sage)"/>
      <rect x="34" y="70" width="4" height="40" fill="var(--stripe-lavender)"/>
    </svg>
    <p class="footer-contact">Meridian Wealth Management | 555.010.2480 | www.MeridianWealth.com</p>
  </div>
</body>
</html>
```